Kelvorn LLC web design project

Dallas, TX based water damage mitigation company needs a web site for its new business. The company does water extractions, mitigation, demo, restoration, and reconstruction. We need for the site to have a strong mobile version, and the owners/managers need to be able to edit the site despite having no web design experience. The site needs to look and function, especially the mobile version, similar to marbleforkquiltshop.com if possible.

```html
<!DOCTYPE html>
<html lang="en">
<head>
<meta charset="utf-8">
<title>Kelvorn LLC — Water Damage Mitigation</title>
<link rel="stylesheet" href="https://fonts.googleapis.com/css2?family=Montserrat:wght@400;500;600;700;800&family=Arimo:wght@400;700&display=swap">
<style>
:root{
  --blue:#1a62b7;
  --blue-dark:#124f98;
  --blue-light:#9cc4ee;
  --ink:#222;
  --text:#444;
  --muted:#666;
  --paper:#ffffff;
  --mist:#eef0f3;
  --night:#2a2a2c;
}
*{box-sizing:border-box;margin:0;padding:0}
html,body{width:1200px;height:4222px;overflow:hidden}
body{position:relative;background:var(--paper);font-family:"Arimo",Arial,sans-serif;color:var(--text)}
.abs{position:absolute}
.heading{font-family:"Montserrat",Arial,sans-serif;color:var(--ink);font-size:30px;letter-spacing:.5px}
.heading b{font-weight:700}
.heading span{font-weight:400}
.body-copy{font-size:14.5px;line-height:25.6px;color:var(--text)}
.btn{display:inline-block;background:var(--blue);color:#fff;font-family:"Montserrat",Arial,sans-serif;font-weight:600;font-size:14px;border-radius:23px;text-align:center;line-height:46px;height:46px;text-decoration:none}

/* hero */
.hero-photo{left:0;top:0;width:1200px;height:740px;background:linear-gradient(180deg,#6d6a8e 0%,#b88682 14%,#8c7f82 30%,#5e5a5c 55%,#4a4645 100%)}
.hero-logo{left:114px;top:92px;font-family:"Montserrat",Arial,sans-serif;font-weight:700;color:#fff;font-size:30px;letter-spacing:1px}
.hamburger{left:1032px;top:74px;width:30px}
.hamburger i{display:block;height:4px;background:#fff;margin-bottom:6px;border-radius:2px}
.hero-title{left:0;width:1200px;text-align:center;color:#fff;font-family:"Montserrat",Arial,sans-serif;font-weight:700}
.hero-title.small{top:196px;font-size:58px}
.hero-title.large{top:255px;font-size:104px;letter-spacing:1px}
.hero-arrow{top:290px}

/* about */
.about-bg{left:0;top:580px;width:1200px;height:605px;background:linear-gradient(90deg,#e3e6ea,#f3f4f6 60%,#e9ebee)}
.about-photo{left:164px;top:713px;width:393px;height:380px;background:linear-gradient(160deg,#2a3a55,#5d6f8a 55%,#c9ccd2);border-radius:4px}

/* services */
.card{top:1354px;width:233px;height:351px;background:#fff;box-shadow:0 2px 8px rgba(0,0,0,.16);text-align:center}
.card .photo{height:161px}
.card h3{font-family:"Montserrat",Arial,sans-serif;font-weight:500;font-size:19px;color:var(--ink);margin:25px 0 14px}
.card p{font-size:14px;line-height:25.5px;color:var(--text);padding:0 14px}
.card a{display:block;margin-top:16px;font-family:"Montserrat",Arial,sans-serif;font-weight:700;font-size:13.5px;color:var(--blue);text-decoration:none}
.card.active{background:var(--blue)}
.card.active h3,.card.active p,.card.active a{color:#fff}
.circle-arrow{top:1502px;width:52px;height:52px;border-radius:50%}

/* testimonials */
.testi-photo{left:111px;top:2081px;width:432px;height:315px;border:2px solid #fff;background:linear-gradient(150deg,#8896a8,#c9d1dc 45%,#3d4e78)}
.quote{left:598px;top:2096px;width:478px;text-align:center;color:#fff;font-size:14.5px;line-height:25.7px}
.dot{top:2364px;width:14px;height:14px;border-radius:50%;border:2px solid #fff}

/* contact */
.field{background:#fff;border-radius:4px;font-size:13px;color:#666;padding:16px 14px}

/* footer */
.foot-head{top:3924px;font-family:"Montserrat",Arial,sans-serif;font-weight:500;font-size:21px;color:var(--ink)}
.foot-list{top:3970px;list-style:none;font-size:14.5px;color:#333}
.foot-list li{height:25.7px}
.foot-list li::before{content:"›";margin-right:9px;color:#333}
.social{top:4050px;width:38px;height:38px;border-radius:50%;background:var(--blue)}
</style>
</head>
<body>

<!-- hero -->
<div class="abs hero-photo" role="img" aria-label="Aerial photo of a downtown city skyline at dusk"></div>
<div class="abs hero-logo">KELVORN LLC</div>
<div class="abs hamburger"><i></i><i></i><i></i></div>
<div class="abs hero-title small">WELCOME TO</div>
<div class="abs hero-title large">KELVORN LLC</div>
<svg class="abs hero-arrow" style="left:56px" width="40" height="60" viewBox="0 0 40 60"><path d="M32 4 8 30l24 26" fill="none" stroke="#fff" stroke-width="6"/></svg>
<svg class="abs hero-arrow" style="left:1106px" width="40" height="60" viewBox="0 0 40 60"><path d="M8 4l24 26L8 56" fill="none" stroke="#fff" stroke-width="6"/></svg>

<!-- about -->
<div class="abs about-bg"></div>
<svg class="abs" style="left:0;top:570px" width="1200" height="180" viewBox="0 0 1200 180">
  <polygon points="0,159 557,7 746,102 1200,12 1200,0 0,0" fill="transparent"/>
  <polygon points="0,143 557,-9 746,86 1200,-4 1200,12 746,102 557,7 0,159" fill="var(--blue)"/>
</svg>
<div class="abs about-photo" role="img" aria-label="Photo of a restoration worker cut into a decorative silhouette"></div>
<div class="abs heading" style="left:639px;top:786px"><b>ABOUT</b> <span>US</span></div>
<p class="abs body-copy" style="left:639px;top:838px;width:450px">Lorem ipsum dolor sit amet, consectetur adipiscing elit, sed do eiusmod tempor incididunt ut labore et dolore magna aliqua. Ut enim ad minim veniam, quis nostrud exercitation ullamco laboris nisi ut aliquip ex ea commodo consequat. Duis aute irure dolor in reprehenderit in voluptate velit esse cillum dolore eu fugiat nulla pariatur. Excepteur sint occaecat cupidatat non proident, sunt in culpa qui officia deserunt mollit anim id est laborum.</p>
<a class="abs btn" style="left:639px;top:1044px;width:134px">LEARN MORE</a>

<!-- services -->
<div class="abs heading" style="left:0;width:1175px;top:1274px;text-align:center"><b>OUR</b> <span>SERVICES</span></div>
<div class="abs circle-arrow" style="left:34px;background:var(--blue)"><svg width="52" height="52" viewBox="0 0 52 52"><path d="M29 18l-8 8 8 8" fill="none" stroke="#fff" stroke-width="3"/></svg></div>
<div class="abs circle-arrow" style="left:1110px;background:#fff;box-shadow:0 1px 6px rgba(0,0,0,.2)"><svg width="52" height="52" viewBox="0 0 52 52"><path d="M23 18l8 8-8 8" fill="none" stroke="var(--blue)" stroke-width="3"/></svg></div>

<div class="abs card" style="left:111px">
  <div class="photo" role="img" aria-label="Photo of yellow water pipes with red valves" style="background:linear-gradient(180deg,#d9d4c8,#b89b3a 60%,#8a7430)"></div>
  <h3>Water Extractions</h3>
  <p>Lorem ipsum dolor sit amet, consectetur adipiscing elit, sed do eiusmod tempor</p>
  <a>LEARN MORE</a>
</div>
<div class="abs card active" style="left:359px">
  <div class="photo" role="img" aria-label="Photo of workers laying a drainage channel" style="background:linear-gradient(160deg,#6f6556,#a59c8c 50%,#5b6a3e)"></div>
  <h3>Mitigation</h3>
  <p>Lorem ipsum dolor sit amet, consectetur adipiscing elit, sed do eiusmod tempor</p>
  <a>LEARN MORE</a>
</div>
<div class="abs card" style="left:606px">
  <div class="photo" role="img" aria-label="Photo of a worker restoring a stripped room" style="background:linear-gradient(180deg,#b9a796,#7e6a5c 60%,#5a4038)"></div>
  <h3>Restoration</h3>
  <p>Lorem ipsum dolor sit amet, consectetur adipiscing elit, sed do eiusmod tempor</p>
  <a>LEARN MORE</a>
</div>
<div class="abs card" style="left:854px">
  <div class="photo" role="img" aria-label="Photo of contractors reviewing plans in a building under reconstruction" style="background:linear-gradient(180deg,#d6d3cd,#9c948a 60%,#6e655c)"></div>
  <h3>Reconstruction</h3>
  <p>Lorem ipsum dolor sit amet, consectetur adipiscing elit, sed do eiusmod tempor</p>
  <a>LEARN MORE</a>
</div>

<!-- testimonials -->
<svg class="abs" style="left:0;top:1770px" width="1200" height="880" viewBox="0 0 1200 880" preserveAspectRatio="none">
  <polygon points="0,164 557,8 746,123 1200,8 1200,721 746,820 557,705 0,869" fill="var(--blue)"/>
  <polygon points="0,176 557,20 746,135 1200,20 1200,50 746,160 557,50 0,200" fill="#2a73c6" opacity=".5"/>
</svg>
<div class="abs heading" style="left:0;width:1190px;top:1988px;text-align:center;color:#fff"><b>TESTIMONIALS</b></div>
<div class="abs testi-photo" role="img" aria-label="Photo of a smiling plumber giving a thumbs up beside a water heater"></div>
<p class="abs quote">"Lorem ipsum dolor sit amet, consectetur adipiscing elit, sed do eiusmod tempor incididunt ut labore et dolore magna aliqua. Ut enim ad minim veniam, quis nostrud exercitation ullamco laboris nisi ut aliquip ex ea commodo consequat. Duis aute irure dolor in reprehenderit in voluptate velit esse cillum dolore eu fugiat nulla pariatur. Excepteur sint occaecat cupidatat non proident, sunt in culpa qui officia deserunt mollit anim id est laborum."</p>
<div class="abs" style="left:598px;width:478px;top:2292px;text-align:center;color:#fff;font-family:Montserrat,Arial,sans-serif;font-weight:600;font-size:22px">Lorem ipsum</div>
<div class="abs" style="left:598px;width:478px;top:2324px;text-align:center;color:#7ea7d9;font-size:14px">Lorem ipsum dolor</div>
<div class="abs dot" style="left:807px"></div>
<div class="abs dot" style="left:828px"></div>
<div class="abs dot" style="left:849px;background:#fff"></div>

<!-- company -->
<div class="abs heading" style="left:111px;top:2717px"><b>KELVORN</b> <span>LLC</span></div>
<p class="abs body-copy" style="left:111px;top:2773px;width:492px">Lorem ipsum dolor sit amet, consectetur adipiscing elit, sed do eiusmod tempor incididunt ut labore et dolore magna aliqua. Ut enim ad minim veniam, quis nostrud exercitation ullamco laboris nisi ut aliquip ex ea commodo consequat. Duis aute irure dolor in reprehenderit in voluptate velit esse cillum dolore eu fugiat nulla pariatur. Excepteur sint occaecat cupidatat non proident, sunt in culpa qui officia deserunt mollit anim id est laborum.</p>
<a class="abs btn" style="left:112px;top:2986px;width:136px">LEARN MORE</a>
<div class="abs" style="left:728px;top:2790px;width:336px;height:230px;border-radius:50%;background:var(--blue-light);transform:rotate(-8deg)"></div>
<div class="abs" style="left:800px;top:2685px;width:220px;height:446px;border-radius:30px;background:#f4f6fb;border:3px solid #c8d2e4;box-shadow:0 14px 30px rgba(90,90,220,.3)">
  <div style="position:absolute;left:10px;top:14px;right:10px;bottom:14px;border-radius:20px;background:var(--blue)"></div>
  <div style="position:absolute;left:0;width:100%;top:232px;text-align:center;color:#fff;font-family:Montserrat,Arial,sans-serif;font-weight:700;font-size:21px">KELVORN LLC</div>
</div>

<!-- contact -->
<svg class="abs" style="left:0;top:3100px" width="1200" height="800" viewBox="0 0 1200 800" preserveAspectRatio="none">
  <defs><linearGradient id="nightGrad" x1="0" y1="0" x2="1" y2="1"><stop offset="0" stop-color="#3a3633"/><stop offset=".5" stop-color="#27272a"/><stop offset="1" stop-color="#1f2024"/></linearGradient></defs>
  <polygon points="0,170 557,14 746,137 1200,22 1200,629 746,744 557,629 0,784" fill="url(#nightGrad)" role="img" aria-label="Dark photo of a technician repairing a wall"/>
  <polyline points="0,170 557,14 746,137 1200,22" fill="none" stroke="var(--blue)" stroke-width="8"/>
  <polyline points="0,784 557,629 746,744 1200,629" fill="none" stroke="var(--blue)" stroke-width="8"/>
</svg>
<div class="abs" style="left:0;width:1200px;top:3284px;text-align:center;color:#fff;font-family:Montserrat,Arial,sans-serif;font-weight:600;font-size:14px">CONTACT US</div>
<div class="abs" style="left:0;width:1200px;top:3306px;text-align:center;color:#fff;font-family:Montserrat,Arial,sans-serif;font-size:31px"><b style="font-weight:600">Get in</b> touch</div>
<div class="abs field" style="left:357px;top:3381px;width:238px;height:49px">First Name</div>
<div class="abs field" style="left:605px;top:3381px;width:238px;height:49px">Last Name</div>
<div class="abs field" style="left:357px;top:3442px;width:238px;height:49px">Phone</div>
<div class="abs field" style="left:605px;top:3442px;width:238px;height:49px">Email</div>
<div class="abs field" style="left:357px;top:3504px;width:486px;height:94px">Message</div>
<a class="abs btn" style="left:533px;top:3613px;width:134px;height:45px;line-height:45px">SUBMIT NOW</a>

<!-- footer -->
<div class="abs" style="left:111px;top:3988px;font-family:Montserrat,Arial,sans-serif;font-weight:700;font-size:31px;color:var(--blue)">KELVORN LLC</div>
<div class="abs social" style="left:111px"></div>
<div class="abs social" style="left:164px"></div>
<div class="abs social" style="left:216px"></div>
<div class="abs social" style="left:267px"></div>

<div class="abs foot-head" style="left:397px">QUICK LINK</div>
<ul class="abs foot-list" style="left:397px"><li>Home</li><li>Consulting</li><li>Repair</li><li>Testimonials</li><li>Contact</li></ul>
<div class="abs foot-head" style="left:610px">COMPANY</div>
<ul class="abs foot-list" style="left:610px"><li>Terms&amp;condtions</li><li>Privacy Policy</li><li>About Us</li><li>Support</li></ul>
<div class="abs foot-head" style="left:838px">CONTACT US</div>
<svg class="abs" style="left:838px;top:3975px" width="14" height="18" viewBox="0 0 14 18"><path d="M7 0a7 7 0 0 0-7 7c0 5 7 11 7 11s7-6 7-11a7 7 0 0 0-7-7zm0 10a3 3 0 1 1 0-6 3 3 0 0 1 0 6z" fill="#222"/></svg>
<div class="abs" style="left:863px;top:3972px;width:210px;font-size:14.5px;line-height:25.7px;color:#333">Lorem ipsum dolor sit amet, consectetur adipiscing</div>
<svg class="abs" style="left:838px;top:4042px" width="15" height="15" viewBox="0 0 24 24"><path d="M6.6 10.8a15 15 0 0 0 6.6 6.6l2.2-2.2a1 1 0 0 1 1-.2 11 11 0 0 0 3.6.6 1 1 0 0 1 1 1V20a1 1 0 0 1-1 1A17 17 0 0 1 3 4a1 1 0 0 1 1-1h3.5a1 1 0 0 1 1 1c0 1.2.2 2.4.6 3.6a1 1 0 0 1-.3 1z" fill="#222"/></svg>
<div class="abs" style="left:863px;top:4040px;font-size:14.5px;color:#333">+1 (888) 888 8888</div>
<svg class="abs" style="left:838px;top:4090px" width="16" height="12" viewBox="0 0 16 12"><rect width="16" height="12" rx="1" fill="#222"/><path d="M0 1l8 6 8-6" fill="none" stroke="#fff" stroke-width="1.4"/></svg>
<div class="abs" style="left:863px;top:4085px;font-size:14.5px;color:#333">info@kelvornllc.com</div>

<div class="abs" style="left:1150px;top:3925px;width:56px;height:50px;border-radius:50%;background:var(--blue)">
  <svg width="50" height="50" viewBox="0 0 50 50"><circle cx="16" cy="25" r="3" fill="#fff"/><circle cx="26" cy="25" r="3" fill="#fff"/><circle cx="36" cy="25" r="3" fill="#fff"/></svg>
</div>

<div class="abs" style="left:111px;top:4146px;width:978px;height:1px;background:#ddd"></div>
<div class="abs" style="left:0;width:1200px;top:4168px;text-align:center;font-size:14.5px;color:#333">©Copyrights 2022 Kelvorn LLC &nbsp;| &nbsp; All Rights Reserved</div>
<div class="abs" style="left:1053px;top:4160px;width:32px;height:32px;border-radius:4px;background:var(--blue-light)"></div>
</body>
</html>
```